Gas utility and appliance store needs awesome web design

Hearthline Supply is a South African based brick and mortar shop looking to improve it's on-line presence.
We cover the whole gambit or products, appliances, information, services, installations and utility related to domestic gas (in SA still considered an alternative fuel) with our most important offerings being the sale of the gas (LPG) itself in combination with high end kitchen and household gas based appliances (stoves, cookers, heaters, fireplaces etc)
Wesite needs to portray our professional (been in the market since 47), family owned (3'rd gen now) roots - it should create the impression of a market leader - and must also portray our domestic (read man in the street) focus and practical approach.
Something professional but light-hearted enough for the general public.
Design must reinforce the belief that LPG is a green,safe and affordable fuel option for domestic use

Target Market(s)

upper middle class market 25-70

Industry/Entity Type

Appliance

Requirements
Must have
• landing page
our company
sustainability
contact us page
menu bar with links to pages (shop, specific information etc)

```html
<!DOCTYPE html>
<html lang="en">
<head>
<meta charset="utf-8">
<title>Hearthline Supply</title>
<link rel="stylesheet" href="https://fonts.googleapis.com/css2?family=Questrial&family=Arimo:wght@400;700&family=Noto+Sans:wght@400;700&display=swap">
<style>
:root{
  --blue:#0b7fd3;
  --blue-soft:#8fb9d6;
  --ink:#222;
  --grey-text:#555;
  --muted:#777;
  --topbar:#e9e9e9;
  --hero:#e9e6e5;
  --rule:#c8c4c4;
  --card-border:#cfcfcf;
  --bottombar:#cdc9ca;
}
*{margin:0;padding:0;box-sizing:border-box}
html,body{width:1200px;height:1147px;overflow:hidden;background:#fff}
.page{position:relative;width:1360px;height:1300px;transform:scale(0.882353);transform-origin:0 0;font-family:"Noto Sans",sans-serif;color:var(--ink)}
.abs{position:absolute}
a{color:inherit;text-decoration:none}

.topbar{left:0;top:0;width:1360px;height:36px;background:var(--topbar)}
.toplinks{top:9px;font-size:13px;color:#333;white-space:nowrap}
.toplinks .phone{color:var(--blue);font-size:15px}
.toplinks .sep{position:absolute;top:3px;width:1px;height:11px;background:#555}

.brand{left:258px;top:0;width:186px;height:292px;background:#fff;border:1px solid #bbb;border-top:none;display:flex;flex-direction:column;align-items:center;justify-content:center;gap:22px}
.brand-dot{width:42px;height:42px;border-radius:50%;background:var(--blue)}
.brand-name{font-family:"Questrial",sans-serif;font-size:28px;line-height:34px;color:var(--blue);text-align:center}

.search{left:854px;top:66px;width:307px;height:34px;display:flex}
.search-field{flex:1;border:1px solid #c9c9c9;border-right:none;border-radius:3px 0 0 3px;font-family:"Arimo",sans-serif;font-style:italic;font-size:12px;color:#777;padding:10px 11px}
.search-btn{width:33px;background:var(--blue);border-radius:0 3px 3px 0;display:flex;align-items:center;justify-content:center}

.nav{left:526px;top:132px;width:634px;height:52px;border:1px solid #cfcfcf;border-radius:14px;background:linear-gradient(#fbfbfb,#e2e2e2);display:flex;font-family:"Questrial",sans-serif;font-size:20px;color:#444}
.nav a{display:flex;align-items:center;justify-content:center;border-left:1px solid #cfcfcf}
.nav a:first-child{border-left:none}

.hero{left:0;top:206px;width:1360px;height:357px;background:var(--hero)}
.hero-rule{left:0;top:563px;width:1360px;height:5px;background:var(--rule)}
.hero-photo{left:200px;top:206px;width:653px;height:357px;background:radial-gradient(ellipse at 62% 55%,#c9c2bb 0%,#8a6d55 28%,#5a3a22 55%,#2a1a10 100%)}
.hero-title{left:905px;top:224px;font-family:"Questrial",sans-serif;font-size:36px;line-height:35px;color:var(--grey-text)}
.hero-text{left:906px;top:351px;width:230px;font-size:15px;line-height:16px;color:var(--grey-text)}
.btn{left:926px;top:436px;width:159px;height:39px;border-radius:8px;background:var(--blue);color:#fff;font-family:"Arimo",sans-serif;font-size:17px;display:flex;align-items:center;justify-content:center}
.dots{left:958px;top:510px;display:flex;gap:14px}
.dots span{width:14px;height:14px;border-radius:50%;background:var(--blue-soft)}
.dots span.on{background:var(--blue)}

.card{top:590px;height:251px;border:1px solid var(--card-border);border-radius:12px;background:linear-gradient(#fff,#f1f1f1)}
.card-title{position:absolute;left:21px;right:21px;top:14px;padding-bottom:6px;border-bottom:1px solid #ccc;font-family:"Questrial",sans-serif;font-size:18px;color:var(--blue)}
.card-text{position:absolute;left:21px;top:55px;font-family:"Arimo",sans-serif;font-size:12px;line-height:14.4px;color:#444}
.card-img{position:absolute}
.more{position:absolute;left:21px;bottom:23px;font-family:"Arimo",sans-serif;font-size:12.5px;color:var(--muted);display:flex;align-items:center;gap:20px}

.footer{left:0;top:866px;width:1360px;height:182px;border-top:1px solid #ddd;background:linear-gradient(#fff,#e9e7e7)}
.fcol{top:881px;font-size:13px;line-height:20px}
.fcol h3{font-size:13px;font-weight:700;display:inline-block;padding-bottom:2px;border-bottom:1px solid var(--blue);margin-bottom:12px}
.fcol li{list-style:none}
.social{left:1006px;top:917px;display:flex;gap:8px}
.social span{width:24px;height:24px;background:#8a8a8a;border-radius:2px}
.bottombar{left:0;top:1048px;width:1360px;height:49px;background:var(--bottombar);font-family:"Arimo",sans-serif;font-size:12.5px;color:#555}
.bottombar strong{font-size:14px;color:#555;margin:0 8px 0 10px}
</style>
</head>
<body>
<div class="page">
  <div class="abs topbar"></div>
  <div class="abs toplinks" style="left:628px">Customer Service <span class="phone" style="margin-left:9px">(011) 482-3190</span></div>
  <div class="abs toplinks" style="left:889px">Where to buy</div>
  <div class="abs toplinks" style="left:1017px">About Us</div>
  <div class="abs toplinks" style="left:1114px">Contact</div>
  <span class="abs toplinks sep" style="left:872px;top:12px"></span>
  <span class="abs toplinks sep" style="left:994px;top:12px"></span>
  <span class="abs toplinks sep" style="left:1095px;top:12px"></span>

  <div class="abs brand">
    <span class="brand-dot"></span>
    <div class="brand-name">Hearthline<br>Supply</div>
  </div>

  <div class="abs search">
    <div class="search-field">Search</div>
    <div class="search-btn">
      <svg width="20" height="20" viewBox="0 0 20 20"><circle cx="8.5" cy="8.5" r="6" fill="none" stroke="#fff" stroke-width="2.4"/><line x1="13" y1="13" x2="18" y2="18" stroke="#fff" stroke-width="2.6" stroke-linecap="round"/></svg>
    </div>
  </div>

  <nav class="abs nav">
    <a style="width:108px">Home</a>
    <a style="width:122px">Products</a>
    <a style="width:143px">Appliances</a>
    <a style="width:110px">Services</a>
    <a style="width:149px">Installation</a>
  </nav>

  <div class="abs hero"></div>
  <div class="abs hero-photo" role="img" aria-label="Steel saucepan on a lit gas stove burner"></div>
  <div class="abs hero-rule"></div>
  <h1 class="abs hero-title" style="font-weight:400">LPG fuel -<br>cleaner than<br>petrol</h1>
  <p class="abs hero-text">Lorem Ipsum. Proin gravida nibh vel velit auctor aliquet. Aenean sollicitudin, lorem</p>
  <a class="abs btn">Read More</a>
  <div class="abs dots"><span></span><span class="on"></span><span></span><span></span></div>

  <section class="abs card" style="left:200px;width:308px">
    <h2 class="card-title" style="font-weight:400">LPG - Green Natural Gas</h2>
    <p class="card-text" style="width:262px">Lorem Ipsum. Proin gravida nibh vel velit auctor aliquet. Aenean sollicitudin, lorem quis bibendum auctor, nisi elit consequat ipsum, nec sagittis sem nibh id elit. Duis sed odio sit amet nibh vulputate cursus a sit amet mauris. Morbi accumsan ipsum velit. Nam nec<br>tellus a odio tincidunt auctor a<br>ornare odio.&nbsp; sequat auctor eu in<br>elit. Class aptent taciti sociosqu<br>ad.</p>
    <div class="card-img" style="left:196px;top:140px;width:88px;height:95px;background:radial-gradient(ellipse at 50% 50%,#8bc34a,#4e8f22 70%,#f1f1f1 72%)" role="img" aria-label="Green LPG gas cylinder"></div>
    <div class="more">Find out more <svg width="13" height="13" viewBox="0 0 13 13"><circle cx="6.5" cy="6.5" r="6.5" fill="var(--blue)"/><path d="M3 6.5h6M6.5 3.8l2.7 2.7-2.7 2.7" stroke="#fff" stroke-width="1.6" fill="none"/></svg></div>
  </section>

  <section class="abs card" style="left:527px;width:306px">
    <h2 class="card-title" style="font-weight:400;left:17px">Services</h2>
    <p class="card-text" style="left:17px;width:270px">Lorem Ipsum. Proin gravida nibh vel velit auctor aliquet. Aenean sollicitudin, lorem quis bibendum auctor, nisi elit consequat ipsum, nec sagittis sem nibh id elit. . Morbi accumsan ipsum velit. Nam nec tellus a odio tincidunt auctor a ornare odio.<br>Sed non&nbsp; mauris<br>vitae erat consequat<br>auctor eu in elit.<br>Class aptent taciti<br>sociosqu</p>
    <div class="card-img" style="left:140px;top:135px;width:144px;height:95px;background:linear-gradient(135deg,#c9c3bb,#8d7a66 55%,#5b4a3c)" role="img" aria-label="Technician installing a gas connection"></div>
    <div class="more" style="left:17px;bottom:25px">Find out more <svg width="13" height="13" viewBox="0 0 13 13"><circle cx="6.5" cy="6.5" r="6.5" fill="var(--blue)"/><path d="M3 6.5h6M6.5 3.8l2.7 2.7-2.7 2.7" stroke="#fff" stroke-width="1.6" fill="none"/></svg></div>
  </section>

  <section class="abs card" style="left:854px;width:306px">
    <h2 class="card-title" style="font-weight:400;left:17px">Products</h2>
    <p class="card-text" style="left:21px;width:250px;top:54px">Lorem Ipsum. Proin gravida nibh vel velit auctor aliquet. Aenean sollicitudin, lorem quis bibendum auctor, nisi elit consequat ipsum, nec sagittis sem nibh id elit. Duis sed odio sit<br>amet nibh vulputate<br>cursus a sit amet<br>mauris. Morbi accum-<br>sa odio lorem quis<br>bibendum lorem quis<br>bibend.</p>
    <div class="card-img" style="left:153px;top:127px;width:132px;height:99px;background:linear-gradient(160deg,#f5f5f5,#c9c9c9 60%,#6b6b6b)" role="img" aria-label="White freestanding gas stove"></div>
    <div class="more" style="bottom:24px">Find out more <svg width="13" height="13" viewBox="0 0 13 13"><circle cx="6.5" cy="6.5" r="6.5" fill="var(--blue)"/><path d="M3 6.5h6M6.5 3.8l2.7 2.7-2.7 2.7" stroke="#fff" stroke-width="1.6" fill="none"/></svg></div>
  </section>

  <footer class="abs footer"></footer>
  <div class="abs fcol" style="left:225px"><h3>Company</h3><ul><li>Certifications</li><li>Customers</li><li>Locations</li><li>Leadership</li><li>Community</li><li>History</li></ul></div>
  <div class="abs fcol" style="left:495px"><h3>Products</h3><ul><li>Stoves</li><li>Cookers</li><li>Heaters</li><li>Fireplaces</li></ul></div>
  <div class="abs fcol" style="left:700px"><h3>Contact Information</h3><ul><li>Hearthline Supply</li><li>14 Kloof Road</li><li>Parkview, Johannesburg 2193</li><li>hello@hearthlinesupply.co.za</li><li>Phone: (011) 482-3191</li><li>Fax: (011) 482-3192</li></ul></div>
  <div class="abs fcol" style="left:1005px;top:882px"><h3 style="padding-right:42px">Connect with us</h3></div>
  <div class="abs social"><span></span><span></span><span></span><span></span><span></span></div>

  <div class="abs bottombar">
    <div class="abs" style="left:221px;top:19px">Copyright © 2012 <strong>Hearthline Supply.</strong> All Rights Reserved</div>
    <div class="abs" style="left:974px;top:19px">Privacy Policy</div>
    <div class="abs" style="left:1071px;top:19px">Term of Use</div>
  </div>
</div>
</body>
</html>
```